Cover design for new academic journal on deconstruction and psychoanalysis

We need a cover for a new academic journal on deconstruction and psychoanalysis. The name of the journal is "The Suspended Threshold: A Journal of Deconstruction and Psychoanalysis" (ST) and it is published by the Halvern College Press(HCP).

Here is a description of the journal on the HCP website:

http://www.halvernpress.example.edu/product/The-Suspended-Threshold,318264.aspx

We are looking for a design that is more abstract and does not have icons or photographs of people, especially not photos of Kovalt or Brisk. The design should be contemporary with clean lines and simple fonts. Again, it should be abstract, with no icons or iconography.

The cover should simply have the full name of the journal and then "Volume 1, Issue 1, 2014" on the cover and "Vol. 1, No. 1, 2014" on the spine.

Attached you can see some ideas that we rejected from HCP. It is important that you understand that these designs were rejected and are just being offered as examples of what the cover will look like in general, as a template of sorts.

The cover should have a bold abstract design, with a space for the title and "Volume 1, Issue 1, 2014."

Something bold and contemporary.

Target Market(s)

Academics, scholars and psychoanalysts.

Industry/Entity Type

University

Font styles to use
Sans Serif

Requirements
Must have
• Must be abstract, bold, have color, and must be contemporary.
Should not have
• No icons, no photographs of Kovalt, Brisk, or anyone.

```html
<!DOCTYPE html>
<html lang="en">
<head>
<meta charset="utf-8">
<title>The Suspended Threshold — Cover Spread</title>
<link rel="stylesheet" href="https://fonts.googleapis.com/css2?family=Didact+Gothic&display=swap">
<style>
  :root {
    --blue: #8f8fec;
    --blue-soft: #e0e0fa;
    --red: #f09292;
    --red-soft: #fbe0e0;
    --green: #9ceb9c;
    --green-soft: #e3fae3;
    --spine-green: #7ee07e;
    --spine-red: #f08a8a;
    --spine-blue: #8a8aee;
    --paper: #ffffff;
    --ink: #111111;
  }
  html, body { margin: 0; padding: 0; overflow: hidden; background: var(--paper); }
  .spread {
    position: relative;
    width: 1200px; height: 692px;
    overflow: hidden;
    background: var(--paper);
    font-family: "Didact Gothic", "Century Gothic", Arial, sans-serif;
    color: var(--ink);
  }
  .artwork { position: absolute; top: 0; height: 650px; }
  .artwork--back { left: 0; width: 590px; }
  .artwork--front { left: 612px; width: 588px; }
  .band {
    position: absolute; top: 0; height: 650px;
    background: linear-gradient(to bottom, var(--c) 0%, var(--c) 50%, var(--s) 100%);
  }
  .band--blue { --c: var(--blue); --s: var(--blue-soft); }
  .band--red { --c: var(--red); --s: var(--red-soft); }
  .band--green { --c: var(--green); --s: var(--green-soft); }

  .spine { position: absolute; left: 590px; top: 0; width: 22px; height: 692px; }
  .spine__seg { position: absolute; left: 2px; width: 18px; }
  .spine__seg--green { top: 0; height: 230px; background: var(--spine-green); }
  .spine__seg--red { top: 230px; height: 232px; background: var(--spine-red); }
  .spine__seg--blue { top: 462px; height: 230px; background: linear-gradient(to bottom, var(--spine-blue), var(--blue-soft)); }
  .spine__label {
    position: absolute; left: 611px; top: 240px;
    transform-origin: 0 0; transform: rotate(90deg);
    font-size: 18px; white-space: nowrap; color: var(--ink);
  }

  .outlined {
    text-shadow:
      -2px 0 var(--paper), 2px 0 var(--paper), 0 -2px var(--paper), 0 2px var(--paper),
      -1.5px -1.5px var(--paper), 1.5px 1.5px var(--paper), -1.5px 1.5px var(--paper), 1.5px -1.5px var(--paper);
  }
  .back-blurb {
    position: absolute; left: 36px; top: 57px; width: 518px; margin: 0;
    font-size: 18px; line-height: 22px; text-align: justify;
  }
  .front-title {
    position: absolute; left: 612px; width: 588px; top: 194px; margin: 0;
    text-align: center; font-weight: 400; font-size: 27px; line-height: 37px;
  }
</style>
</head>
<body>
<main class="spread">
  <div class="artwork artwork--back" role="img" aria-label="Abstract colour field of blue, red and green vertical bands fading downward">
    <div class="band band--blue" style="left:0;width:194px"></div>
    <div class="band band--red" style="left:196px;width:195px"></div>
    <div class="band band--green" style="left:393px;width:197px"></div>
  </div>
  <div class="artwork artwork--front" role="img" aria-label="Abstract colour field of green, red and blue vertical bands fading downward">
    <div class="band band--green" style="left:0;width:195px"></div>
    <div class="band band--red" style="left:197px;width:195px"></div>
    <div class="band band--blue" style="left:394px;width:194px"></div>
  </div>

  <div class="spine">
    <div class="spine__seg spine__seg--green"></div>
    <div class="spine__seg spine__seg--red"></div>
    <div class="spine__seg spine__seg--blue"></div>
  </div>
  <div class="spine__label">Vol. 1, No. 1, 2014</div>

  <p class="back-blurb outlined">Deconstruction—the analysis and transformation of metaphysics—intersects with psychoanalysis. Both are engaged with thinking beyond consciousness. This new journal is a forum for those working at the borders of these two disciplines. Its name, The Suspended Threshold, refers to the broadest aspect of psychoanalysis—the theory of unconscious processes—and to Kovalt's thinking about undecidability—the irreducible oscillation and chance of non-metaphysical processes. The name, then, speaks of psychoanalysis as deconstruction. It also invites opening to all fields in which undecidability is at stake. Hence the journal seeks contributions from all disciplines informed by deconstruction and psychoanalysis. Its aim is to enrich, to expand, to change: deconstruction, psychoanalysis, and everything that they touch upon.</p>

  <h1 class="front-title outlined">The Suspended Threshold:<br>A Journal of Deconstruction and Psychoanalysis<br>Volume 1, Issue 1, 2014</h1>
</main>
</body>
</html>
```